homepage design , industry automation control image

we need a design , based on our Logo image.

we focus on selling of temprature sensor ,and parts.

but need concept or image on industry automation control

we need enviroment friendly concept.

Industry/Entity Type

Industry

Number of Pages Required

5+ page

Requirements
Must have
• we need a Cartoon Image of a Temperature sensor,
• attaching a Excel file with the sensor looking.
Nice to have
• Nature image, future concept

```html
<!DOCTYPE html>
<html lang="en">
<head>
<meta charset="utf-8">
<title>Lind Sensortechnik — Temperature Sensors</title>
<link href="https://fonts.googleapis.com/css2?family=Jost:wght@400;500;600&family=Lato:wght@400;700&display=swap" rel="stylesheet">
<style>
:root{
  --green:#0a8a0a;
  --green-dark:#066806;
  --lime:#8ad600;
  --lime-text:#b6f200;
  --ink:#1b1b1b;
  --text:#4a4a4a;
  --muted:#9a9a9a;
  --line:#d6d6d6;
  --grey-bg:#eeeeee;
  --band:#efefea;
  --footer:#1f1f1f;
  --white:#ffffff;
}
*{box-sizing:border-box;margin:0;padding:0}
html,body{width:1200px;height:2885px;overflow:hidden;background:var(--white)}
body{font-family:"Lato",sans-serif;color:var(--text)}
.page{position:relative;width:1200px;height:2885px;overflow:hidden}
.abs{position:absolute}
.heading{font-family:"Jost",sans-serif;font-weight:400;color:var(--ink)}
.heading em{font-style:normal;color:var(--green)}

/* top bar */
.topbar{left:0;top:0;width:1200px;height:38px;background:var(--green)}
.topbar .contact{top:9px;font-size:14px;color:var(--white);display:flex;align-items:center;gap:10px}
.icon-box{width:22px;height:22px;border:2px solid var(--white);display:flex;align-items:center;justify-content:center}
.search{left:888px;top:0;width:212px;height:38px;background:var(--green-dark);color:var(--white);font-size:12px;padding:11px 12px;font-weight:700}
.search svg{position:absolute;right:12px;top:12px}

/* header */
.logo{left:100px;top:54px;display:flex;align-items:center;gap:10px}
.logo .mark{width:57px;height:57px;background:var(--lime);border:3px solid var(--green)}
.logo .name{font-family:"Jost",sans-serif;font-weight:500;font-size:31px;color:var(--green)}
.nav{top:76px;font-family:"Jost",sans-serif;font-size:14px;color:var(--ink)}
.nav.active{color:var(--green)}

/* hero */
.hero{left:0;top:125px;width:1200px;height:554px;background:linear-gradient(180deg,#7aa5cf 0%,#b7cde2 38%,#d9e2e8 52%,#5f8a4c 60%,#6f8f5b 70%,#8fa0a8 76%,#6d8696 100%)}
.hero-box{left:100px;top:338px;width:454px;height:127px;background:rgba(20,20,20,.85);padding:14px 18px}
.hero-box h1{font-family:"Jost",sans-serif;font-weight:500;font-size:29px;line-height:36px;color:var(--white)}
.hero-box h1 span{color:var(--lime-text)}
.hero-box p{font-size:15px;color:var(--white);margin-top:8px}
.btn{background:var(--green);color:var(--white);font-family:"Jost",sans-serif;border:2px solid var(--lime);display:flex;align-items:center;justify-content:center}
.hero-btn{left:119px;top:479px;width:162px;height:44px;font-size:17px;box-shadow:0 0 0 3px var(--green)}
.hero-product{left:612px;top:260px;width:200px;height:200px;border-radius:50%;background:radial-gradient(circle,#d8dadc 0%,#9ea3a8 60%,#ffffff 62%)}

/* section titles */
.sec-title{left:0;width:1200px;text-align:center;font-size:33px}
.divider{left:323px;width:554px;height:1px;background:var(--line)}
.divider-mark{width:18px;height:16px;background:#a7a7a7;border:2px solid #e5e5e5}
.lead{left:110px;width:980px;text-align:center;font-size:13px;line-height:22px;color:var(--text)}
.lead a{color:var(--green);text-decoration:underline;font-weight:700}

/* about */
.about-band{left:0;top:1033px;width:1200px;height:255px;background:var(--band)}
.about-curve{left:0;top:1033px}
.cat-ring{width:212px;height:212px;border-radius:50%;background:var(--white);box-shadow:0 2px 10px rgba(0,0,0,.08);display:flex;align-items:center;justify-content:center}
.cat-circle{width:180px;height:180px;border-radius:50%;background:var(--green)}
.cat-title{width:320px;text-align:center;font-family:"Jost",sans-serif;font-size:21px;color:var(--ink)}
.cat-text{width:320px;text-align:center;font-size:13px;line-height:20px}
.plus{width:22px;height:22px;border:2px solid var(--green);color:var(--green);font-weight:700;font-size:17px;line-height:16px;text-align:center}

/* advantage */
.adv-box{width:66px;height:66px;background:var(--green);border:3px solid var(--white);box-shadow:0 0 0 2px var(--green);display:flex;align-items:center;justify-content:center}
.adv-label{font-family:"Jost",sans-serif;font-size:17px;color:var(--ink)}
.adv-center{left:540px;top:1644px;width:120px;height:119px;background:linear-gradient(135deg,var(--lime),var(--green));border:3px solid var(--white);box-shadow:0 0 0 2px var(--lime);display:flex;align-items:center;justify-content:center;text-align:center;font-family:"Jost",sans-serif;font-weight:500;font-size:15px;line-height:19px;color:var(--white)}

/* cta */
.cta{left:0;top:1802px;width:1200px;height:117px;background:linear-gradient(90deg,#101010,#1f1f1f 60%,#141414)}
.cta h2{position:absolute;left:100px;top:40px;font-family:"Jost",sans-serif;font-weight:400;font-size:28px;color:var(--white)}
.cta-btn{left:938px;top:1838px;width:162px;height:46px;background:var(--lime);color:var(--white);font-size:17px;border:2px solid var(--green);box-shadow:0 0 0 2px var(--lime)}

/* news & testimonials */
.news-wrap{left:0;top:1919px;width:1200px;height:346px;background:var(--grey-bg)}
.col-title{font-size:31px;top:1960px}
.arrow{width:24px;height:24px;border:2px solid #9a9a9a;display:flex;align-items:center;justify-content:center}
.arrow.on{border-color:var(--green)}
.col-rule{height:1px;background:var(--line)}
.date{left:100px;width:50px;height:54px;text-align:center;font-family:"Jost",sans-serif}
.date .d{height:30px;background:#2a2a2a;color:var(--white);font-size:20px;line-height:30px;font-weight:500}
.date .m{height:24px;background:var(--green);color:var(--white);font-size:12px;line-height:24px}
.news-title{left:169px;font-family:"Jost",sans-serif;font-size:17px;color:var(--ink)}
.news-text{left:169px;width:405px;font-size:12.5px;line-height:21px}
.photo{left:627px;top:2063px;width:109px;height:108px;background:linear-gradient(160deg,#c9d6e2,#6f8497);border:3px solid var(--white);box-shadow:0 0 0 2px var(--lime)}
.quote{left:769px;top:2068px;width:331px;font-size:12.5px;line-height:25px;letter-spacing:1.2px;text-indent:24px}
.quote-mark{font-family:"Jost",sans-serif;font-size:36px;color:#c8c8c8;line-height:1}
.author{left:769px;top:2174px;font-family:"Jost",sans-serif;font-size:18px;color:var(--green)}

/* call back */
.cb-title{left:100px;top:2300px;font-size:36px;line-height:44px}
.cb-text{left:100px;top:2412px;width:300px;font-size:12.5px;line-height:21px}
.form-label{left:460px;top:2310px;font-size:14px;color:var(--ink)}
.field{height:39px;border:1px solid var(--line);font-size:12px;color:var(--text);padding:12px 10px}
.submit{left:460px;top:2458px;width:105px;height:38px;background:var(--green);color:var(--white);font-size:15px;display:flex;align-items:center;justify-content:center;font-family:"Jost",sans-serif}

/* footer */
.footer{left:0;top:2538px;width:1200px;height:302px;background:var(--footer)}
.f-title{top:2588px;font-family:"Jost",sans-serif;font-size:20px;color:var(--white)}
.f-rule{top:2627px;height:1px;background:#444}
.f-rule i{position:absolute;left:0;top:-1px;width:40px;height:2px;background:var(--lime)}
.f-links{left:100px;top:2644px;list-style:none;font-size:13px;line-height:27px;color:#cfcfcf}
.f-links li::before{content:"›";color:var(--lime);margin-right:8px}
.f-links li.on{color:var(--lime)}
.f-text{font-size:13px;line-height:20px;color:#bcbcbc}
.f-line{display:flex;align-items:center;gap:12px;color:#d8d8d8}
.news-panel{left:538px;top:2580px;width:274px;height:240px;border:1px solid #2b2b2b}
.news-input{left:552px;top:2713px;width:209px;height:35px;background:#3a3a3a;color:#dcdcdc;font-size:12px;padding:11px 10px}
.sub-btn{left:552px;top:2762px;width:119px;height:38px;font-size:15px;box-shadow:0 0 0 2px var(--green)}
.f-logo-mark{left:947px;top:2640px;width:56px;height:54px;background:#555;border:2px solid #888}
.f-logo-name{left:830px;top:2700px;width:290px;text-align:center;font-family:"Jost",sans-serif;font-size:27px;color:#cfcfcf}
.social{top:2752px;width:26px;height:26px;background:#1b6fbf;border:1px solid #fff}
.copyright{left:0;top:2840px;width:1200px;height:45px;background:var(--green);color:var(--white);font-size:13px;font-weight:700;text-align:center;line-height:45px}
</style>
</head>
<body>
<div class="page">

  <!-- top bar -->
  <div class="abs topbar"></div>
  <div class="abs contact topbar-contact" style="left:100px;top:8px;display:flex;align-items:center;gap:10px;color:#fff;font-size:14px">
    <span class="icon-box"><svg width="12" height="12" viewBox="0 0 24 24"><path fill="#fff" d="M6.6 10.8a15 15 0 0 0 6.6 6.6l2.2-2.2c.3-.3.7-.4 1-.2 1.1.4 2.3.6 3.6.6.6 0 1 .4 1 1V20c0 .6-.4 1-1 1A17 17 0 0 1 3 4c0-.6.4-1 1-1h3.5c.6 0 1 .4 1 1 0 1.2.2 2.4.6 3.6.1.3 0 .7-.2 1z"/></svg></span>
    <span>555.014.2290</span>
    <span class="icon-box" style="margin-left:22px"><svg width="12" height="10" viewBox="0 0 24 18"><rect x="1" y="1" width="22" height="16" fill="none" stroke="#fff" stroke-width="2"/><path d="M1 1l11 9 11-9" fill="none" stroke="#fff" stroke-width="2"/></svg></span>
    <span>info@lindsensortechnik.com</span>
  </div>
  <div class="abs search">Search...
    <svg width="14" height="14" viewBox="0 0 24 24"><circle cx="10" cy="10" r="7" fill="none" stroke="#fff" stroke-width="3"/><path d="M15 15l7 7" stroke="#fff" stroke-width="3"/></svg>
  </div>

  <!-- header -->
  <div class="abs logo"><span class="mark"></span><span class="name">Lind Sensortechnik</span></div>
  <span class="abs nav active" style="left:610px">Home</span>
  <span class="abs nav" style="left:686px">About Us</span>
  <span class="abs nav" style="left:779px">Services</span>
  <span class="abs nav" style="left:867px">Products</span>
  <span class="abs nav" style="left:956px">News</span>
  <span class="abs nav" style="left:1029px">Contact Us</span>

  <!-- hero -->
  <div class="abs hero" role="img" aria-label="Photo of a river landscape with a bridge, trees and a tall building under a cloudy sky"></div>
  <div class="abs hero-product" role="img" aria-label="Photo of a temperature sensor with connection head"></div>
  <div class="abs hero-box">
    <h1>15 years experience<br>in <span>Temperature Sensor Industry</span></h1>
    <p>Lorem ipsum dolor sit amet, consectetur adipiscing elit.</p>
  </div>
  <div class="abs btn hero-btn">Contact Now</div>

  <!-- about -->
  <h2 class="abs heading sec-title" style="top:714px">About <em>Lind Sensortechnik</em></h2>
  <div class="abs divider" style="top:789px"></div>
  <div class="abs divider-mark" style="left:591px;top:781px"></div>
  <p class="abs lead" style="top:820px">Lorem ipsum dolor sit amet, consectetuer adipiscing elit, sed diam nonummy nibh euismod tincidunt ut laoreet dolore magna aliquam erat volutpat. Ut wisi enim ad minim veniam, quis nostrud exerci tation ullamcorper suscipit lobortis nisl ut aliquip ex ea commodo consequat. Duis autem vel eum iriure dolor in hendrerit in vulputate velit esse molestie consequat, vel illum dolore eu feugiat nulla facilisis at vero eros et accumsan ... <a>Read More</a></p>

  <div class="abs about-band"></div>
  <svg class="abs about-curve" width="300" height="255" viewBox="0 0 300 255"><path d="M0 0 Q160 40 200 255 L0 255 Z" fill="#e4e4de"/></svg>

  <div class="abs cat-ring" style="left:152px;top:913px"><div class="cat-circle" role="img" aria-label="Illustration of a temperature sensor"></div></div>
  <div class="abs cat-ring" style="left:494px;top:913px"><div class="cat-circle" role="img" aria-label="Illustration of a sensor terminal block part"></div></div>
  <div class="abs cat-ring" style="left:836px;top:913px"><div class="cat-circle" role="img" aria-label="Illustration of a coiled heater element"></div></div>

  <div class="abs cat-title" style="left:98px;top:1132px">Temperature sensor</div>
  <div class="abs cat-title" style="left:440px;top:1132px">Temperature sensor parts</div>
  <div class="abs cat-title" style="left:782px;top:1132px">Heater &amp; Parts</div>
  <p class="abs cat-text" style="left:98px;top:1164px">Lorem ipsum dolor sit amet, consectetur adipiscing elit, sed do eiusmod</p>
  <p class="abs cat-text" style="left:440px;top:1164px">Lorem ipsum dolor sit amet, consectetur adipiscing elit, sed do eiusmod</p>
  <p class="abs cat-text" style="left:782px;top:1164px">Lorem ipsum dolor sit amet, consectetur adipiscing elit, sed do eiusmod</p>
  <div class="abs plus" style="left:247px;top:1213px">+</div>
  <div class="abs plus" style="left:589px;top:1213px">+</div>
  <div class="abs plus" style="left:931px;top:1213px">+</div>

  <!-- advantage -->
  <h2 class="abs heading sec-title" style="top:1324px">Our <em>Advantage</em></h2>
  <div class="abs divider" style="top:1392px"></div>
  <div class="abs divider-mark" style="left:591px;top:1384px"></div>
  <p class="abs lead" style="top:1425px;left:140px;width:920px">Ut enim ad minim veniam, quis nostrud exercitation ullamco laboris nisi ut aliquip ex ea commodo consequat. Duis aute irure dolor in reprehenderit in voluptate velit esse cillum dolore eu fugiat nulla pariatur. Excepteur sint occaecat cupidatat non proident, sunt in culpa qui</p>

  <svg class="abs" style="left:0;top:1500px" width="1200" height="302" viewBox="0 1500 1200 302">
    <circle cx="600" cy="1802" r="244" fill="none" stroke="var(--green)" stroke-width="3"/>
  </svg>

  <div class="abs adv-label" style="left:500px;width:200px;text-align:center;top:1487px">Customized Products</div>
  <div class="abs adv-label" style="right:796px;top:1594px">Long Time Experience</div>
  <div class="abs adv-label" style="left:794px;top:1594px">Quality Guarantee</div>
  <div class="abs adv-label" style="right:870px;top:1700px">Quick Response</div>
  <div class="abs adv-label" style="left:877px;top:1700px">Reliable Credit</div>

  <div class="abs adv-box" style="left:563px;top:1525px">
    <svg width="36" height="36" viewBox="0 0 24 24"><circle cx="12" cy="12" r="7" fill="none" stroke="#fff" stroke-width="2.5" stroke-dasharray="3 2.5"/><circle cx="12" cy="12" r="3" fill="#fff"/></svg>
  </div>
  <div class="abs adv-box" style="left:425px;top:1571px">
    <svg width="32" height="32" viewBox="0 0 24 24"><rect x="4" y="2" width="13" height="18" fill="none" stroke="#fff" stroke-width="2"/><path d="M7 7h7M7 11h7" stroke="#fff" stroke-width="2"/><circle cx="17" cy="17" r="4" fill="#fff"/></svg>
  </div>
  <div class="abs adv-box" style="left:707px;top:1571px">
    <svg width="32" height="32" viewBox="0 0 24 24"><circle cx="12" cy="10" r="7" fill="#fff"/><path d="M8 16l-2 7 6-3 6 3-2-7" fill="#fff"/><circle cx="12" cy="10" r="3" fill="var(--green)"/></svg>
  </div>
  <div class="abs adv-box" style="left:342px;top:1678px">
    <svg width="32" height="32" viewBox="0 0 24 24"><path d="M12 3C6.5 3 2 6.6 2 11c0 2.3 1.2 4.3 3.1 5.8L4 21l4.8-2.6c1 .3 2.1.6 3.2.6 5.5 0 10-3.6 10-8S17.5 3 12 3z" fill="#fff"/><circle cx="8" cy="11" r="1.3" fill="var(--green)"/><circle cx="12" cy="11" r="1.3" fill="var(--green)"/><circle cx="16" cy="11" r="1.3" fill="var(--green)"/></svg>
  </div>
  <div class="abs adv-box" style="left:794px;top:1678px">
    <svg width="32" height="32" viewBox="0 0 24 24"><path d="M12 2l8 3v6c0 5-3.5 9-8 11-4.5-2-8-6-8-11V5z" fill="#fff"/><path d="M8 12l3 3 5-6" fill="none" stroke="var(--green)" stroke-width="2.2"/></svg>
  </div>
  <div class="abs adv-center">Lind<br>Sensortechnik</div>

  <!-- call to action -->
  <div class="abs cta"><h2>Improve Your Productivity With Lind Sensortechnik</h2></div>
  <div class="abs btn cta-btn">Contact Now</div>

  <!-- news -->
  <div class="abs news-wrap"></div>
  <h2 class="abs heading col-title" style="left:100px">Latest <em>News</em></h2>
  <div class="abs arrow" style="left:519px;top:1976px"><svg width="10" height="12" viewBox="0 0 10 12"><path d="M7 1L2 6l5 5" fill="none" stroke="#9a9a9a" stroke-width="2"/></svg></div>
  <div class="abs arrow on" style="left:548px;top:1976px"><svg width="10" height="12" viewBox="0 0 10 12"><path d="M3 1l5 5-5 5" fill="none" stroke="var(--green)" stroke-width="2"/></svg></div>
  <div class="abs col-rule" style="left:100px;top:2027px;width:473px"></div>
  <div class="abs divider-mark" style="left:100px;top:2019px"></div>

  <div class="abs date" style="top:2065px"><div class="d">06</div><div class="m">Mar</div></div>
  <div class="abs news-title" style="top:2062px">Diam Nonummy Nibh Euism Od Tincidunt</div>
  <p class="abs news-text" style="top:2086px">Lorem ipsum dolor sit amet, consectetuer adipiscing elit, sedl diam nonummy nibh euism od tincidunt ut laoreet doloremoi magna</p>
  <div class="abs col-rule" style="left:100px;top:2146px;width:473px"></div>
  <div class="abs date" style="top:2165px"><div class="d">06</div><div class="m">Mar</div></div>
  <div class="abs news-title" style="top:2162px">Diam Nonummy Nibh Euism Od Tincidunt</div>
  <p class="abs news-text" style="top:2186px">Lorem ipsum dolor sit amet, consectetuer adipiscing elit, sedl diam nonummy nibh euism od tincidunt ut laoreet doloremoi magna</p>

  <div class="abs" style="left:600px;top:1960px;width:1px;height:280px;background:var(--line)"></div>

  <!-- testimonials -->
  <h2 class="abs heading col-title" style="left:627px">Client <em>Testimonials</em></h2>
  <div class="abs arrow" style="left:1046px;top:1976px"><svg width="10" height="12" viewBox="0 0 10 12"><path d="M7 1L2 6l5 5" fill="none" stroke="#9a9a9a" stroke-width="2"/></svg></div>
  <div class="abs arrow on" style="left:1075px;top:1976px"><svg width="10" height="12" viewBox="0 0 10 12"><path d="M3 1l5 5-5 5" fill="none" stroke="var(--green)" stroke-width="2"/></svg></div>
  <div class="abs col-rule" style="left:627px;top:2027px;width:473px"></div>
  <div class="abs divider-mark" style="left:627px;top:2019px"></div>
  <div class="abs photo" role="img" aria-label="Portrait photo of the client"></div>
  <span class="abs quote-mark" style="left:750px;top:2062px">“</span>
  <p class="abs quote">Ut enim ad minim veniam, quis nostrud exercitation ullamco laboris nisi ut aliquip ex ea commodo consequat. Duis aute irure dolor in reprehenderit in voluptate velit esse dolore</p>
  <span class="abs quote-mark" style="left:1040px;top:2138px">”</span>
  <div class="abs author">– Mr. Tomas Verhal</div>
  <svg class="abs" style="left:757px;top:2212px" width="88" height="16" viewBox="0 0 88 16">
    <g id="star"><path d="M8 1l2 5h5l-4 3 1.6 5L8 11l-4.6 3L5 9 1 6h5z" fill="var(--green)"/></g>
    <use href="#star" x="17"/><use href="#star" x="34"/>
    <path transform="translate(51 0)" d="M8 1l2 5h5l-4 3 1.6 5L8 11l-4.6 3L5 9 1 6h5z" fill="#a8a8a8"/>
    <path transform="translate(68 0)" d="M8 1l2 5h5l-4 3 1.6 5L8 11l-4.6 3L5 9 1 6h5z" fill="#a8a8a8"/>
  </svg>

  <!-- request a call back -->
  <h2 class="abs heading cb-title">Request<br><em>A Call Back.</em></h2>
  <p class="abs cb-text">Duis autem vel eum iriure dolormi opl inmol hendi rerit in vulpu tateml velitm essemolmi mo molestiel conseqb uat, velmi illum dolorl eokf no atn nulla more facilisis.</p>
  <div class="abs form-label">Please fill up bellow form</div>
  <div class="abs field" style="left:460px;top:2346px;width:313px">Name</div>
  <div class="abs field" style="left:789px;top:2346px;width:311px">Email</div>
  <div class="abs field" style="left:460px;top:2401px;width:313px">Phone</div>
  <div class="abs field" style="left:789px;top:2401px;width:311px">Message</div>
  <div class="abs submit">Submit</div>

  <!-- footer -->
  <div class="abs footer"></div>
  <div class="abs f-title" style="left:100px">Quick Links</div>
  <div class="abs f-rule" style="left:100px;width:122px"><i></i></div>
  <ul class="abs f-links">
    <li class="on">Home</li><li>About Us</li><li>Services</li><li>Products</li><li>News</li><li>Contact Us</li>
  </ul>

  <div class="abs f-title" style="left:263px">Contact Detail</div>
  <div class="abs f-rule" style="left:263px;width:245px"><i></i></div>
  <div class="abs f-text" style="left:263px;top:2644px;width:250px"><span style="color:#e5e5e5">Lind Sensortechnik</span><br>Lorem ipsum dolor sit amet, consectetur adipiscing elit, sed do eiusmod</div>
  <div class="abs f-line" style="left:263px;top:2735px;font-size:17px">
    <svg width="16" height="16" viewBox="0 0 24 24"><path fill="var(--lime)" d="M6.6 10.8a15 15 0 0 0 6.6 6.6l2.2-2.2c.3-.3.7-.4 1-.2 1.1.4 2.3.6 3.6.6.6 0 1 .4 1 1V20c0 .6-.4 1-1 1A17 17 0 0 1 3 4c0-.6.4-1 1-1h3.5c.6 0 1 .4 1 1 0 1.2.2 2.4.6 3.6.1.3 0 .7-.2 1z"/></svg>555.014.2290</div>
  <div class="abs f-line" style="left:263px;top:2779px;font-size:13px">
    <svg width="16" height="12" viewBox="0 0 24 18"><rect width="24" height="18" fill="var(--lime)"/><path d="M1 1l11 9 11-9" fill="none" stroke="var(--footer)" stroke-width="2"/></svg>info@lindsensortechnik.com</div>

  <div class="abs news-panel"></div>
  <div class="abs f-title" style="left:552px">Join Our Newsletter</div>
  <div class="abs f-rule" style="left:552px;width:258px"><i></i></div>
  <p class="abs f-text" style="left:552px;top:2656px;width:230px;font-size:12.5px">Subscribe to our Newsletter to get the latest scoop right to your inbox</p>
  <div class="abs news-input">Enter Your Email</div>
  <div class="abs btn sub-btn">Subscribe</div>

  <div class="abs f-logo-mark"></div>
  <div class="abs f-logo-name">Lind Sensortechnik</div>
  <div class="abs social" style="left:927px"></div>
  <div class="abs social" style="left:962px;background:#1d9bd7"></div>
  <div class="abs social" style="left:997px"></div>

  <div class="abs copyright">© 2017 Lind Sensortechnik. All Rights Reserved.</div>
</div>
</body>
</html>
```